Visitenkarten-Design für private und gesellschaftliche Anlässe gesucht
Zielgruppe
Es handelt sich um eine Visitenkarte für den privaten Bereich, bzw. für private und Gesellschaftliche Anlässe
Aufgabenstellung
Zunächst die Kontaktdaten
Roland Kettwig
Postfach 3087
mail@rolandkettwig.de
Des weiteren soll der Spruch 'Gnothi seauton ' (altgr. Erkenne dich selbst) auf der Karte stehen. Gerne auch auf der Rückseite oder an einer anderen prominenten Stelle
Schön wäre es auch, wenn die I Punkte in meinem Namen farblich etwas hervorgehoben sind und auch so noch einmal an anderer stelle zu finden sind.
Ich habe meine ungefähre Vorstellung als Skizze angehängt, ansonsten gerne auch noch einmal nachfragen.
Ich bin noch etwas unschlüssig, ob die Karte ein klassisches Format erhalten soll oder es doch Quadratisch wird.

```html
<!DOCTYPE html>
<html lang="de">
<head>
<meta charset="utf-8">
<title>Visitenkarte Roland Kettwig</title>
<link rel="stylesheet" href="https://fonts.googleapis.com/css2?family=Playfair+Display:wght@500&family=Barlow:wght@300;400&display=swap">
<style>
  :root {
    --page: #ffffff;
    --ink: #000000;
    --card-gold: #e6cd7b;
    --accent-ochre: #c9994c;
    --accent-wine: #8b1a1a;
    --accent-white: #ffffff;
  }
  html, body {
    margin: 0;
    padding: 0;
    width: 1145px;
    height: 1200px;
    overflow: hidden;
    background: var(--page);
  }
  .sheet {
    position: relative;
    width: 1145px;
    height: 1200px;
  }
  .card {
    position: absolute;
    left: 243px;
    width: 666px;
    height: 431px;
    display: block;
  }
  .card--front { top: 173px; }
  .card--back  { top: 619px; }
  .motto, .name {
    font-family: "Playfair Display", "Bodoni Moda", serif;
    font-weight: 500;
    font-size: 66px;
  }
  .motto { fill: var(--card-gold); }
  .name  { fill: var(--ink); }
  .contact {
    font-family: "Barlow", "Helvetica Neue", sans-serif;
    font-weight: 300;
    font-size: 17.5px;
    letter-spacing: 1.4px;
    fill: var(--ink);
  }
</style>
</head>
<body>
<main class="sheet">

  <svg class="card card--front" viewBox="0 0 666 431" aria-label="Vorderseite: Gnothi sauton">
    <defs>
      <linearGradient id="front-accent" x1="0" y1="0" x2="0" y2="1">
        <stop offset="0" stop-color="var(--accent-ochre)"/>
        <stop offset="0.38" stop-color="var(--card-gold)"/>
        <stop offset="0.7" stop-color="var(--accent-wine)"/>
        <stop offset="1" stop-color="var(--accent-white)"/>
      </linearGradient>
    </defs>
    <rect width="666" height="431" fill="var(--ink)"/>
    <rect class="accent-area" x="306" y="62" width="24" height="310" fill="url(#front-accent)" opacity="0.35"
          role="img" aria-label="Dekoratives Punktmotiv in Ocker, Gold, Weinrot und Weiß"/>
    <text class="motto" x="195" y="229" textLength="276" lengthAdjust="spacingAndGlyphs">Gnothi sauton</text>
  </svg>

  <svg class="card card--back" viewBox="0 0 666 431" aria-label="Rückseite: Roland Kettwig, Kontakt">
    <defs>
      <linearGradient id="back-accent" x1="0" y1="0" x2="0" y2="1">
        <stop offset="0" stop-color="var(--accent-ochre)"/>
        <stop offset="0.4" stop-color="var(--accent-wine)"/>
        <stop offset="0.75" stop-color="var(--accent-white)"/>
        <stop offset="1" stop-color="var(--card-gold)"/>
      </linearGradient>
    </defs>
    <rect width="666" height="431" fill="var(--card-gold)"/>
    <rect class="accent-area" x="243" y="63" width="149" height="275" fill="url(#back-accent)" opacity="0.3"
          role="img" aria-label="Dekoratives Punktmotiv in Ocker, Weinrot, Weiß und Schwarz"/>
    <text class="name" x="187" y="229" textLength="292" lengthAdjust="spacingAndGlyphs">Roland Kettwig</text>
    <text class="contact" x="328" y="376" text-anchor="middle">Postfach 3087 . 12345 Ort?</text>
    <text class="contact" x="328" y="401" text-anchor="middle">+49 1570 4438215 . mail@rolandkettwig.de</text>
  </svg>

</main>
</body>
</html>
```